Web Design Project

Psychotherapy and Counselling Practice needs a landing page web design.

My business "Harbourlight Consulting" specialises in the treatment of Anxiety and Depression with a holistic approach, endeavouring to unlock the key that holds us to ransom in a life that is imbalanced, frustrating, and ultimately of our own making due to our own perceptions and behaviours.

There is much that impacts us which we cannot change, but we are always in control of how we think, and how we frame our experiences.....learning to challenge those thoughts and behaviours that are destructive and disempowering opens up a world of joyful possibility. Life is about making choices, learn to make wiser and healthier choices.......

Harbourlight Consulting has a client base of individual clients but will seek to expand to offer services to the Corporate world by offering an adjunct to employers for established "Wellness Programs".

Harbourlight Consulting is a highly professional, ethically bound business, with the needs of the client at the forefront of all we do.

Harbourlight Consulting wishes to avoid the usual "jargon driven" psychobabble offered on many counselling web pages. It aims to be stylishly presented, clean in look and with as few "words" as possible and a largely white background (faster loading and more powerful impact of what is stated), those words contained in the webpage should be meaningful, persuasive and have an impact simply at glance. Harbourlight does not want , or expect, those prospective clients in need of support , to be reading through volumes of industry driven cliches.

At this point Harbourlight is just looking for a high quality landing page. However in time this will likely expand to include other sections such as case studies, video content etc.

Target Market(s)

Those in need of emotional support, suffering mental health issues, and those simply wanting to become self aware supported by a mindful therapist.

Industry/Entity Type

Industry

Requirements
Must have
• The design must incorporate the Harbourlight logo and colour schemes found on the attached files.

```html
<!DOCTYPE html>
<html lang="en">
<head>
<meta charset="utf-8">
<title>Harbourlight Consulting</title>
<link rel="stylesheet" href="https://fonts.googleapis.com/css2?family=Open+Sans:wght@300;400;600&display=swap">
<style>
:root{
  --green:#8cb21e;
  --green-dark:#7a9c16;
  --band:#6b6b6b;
  --disc:#666666;
  --ink:#555555;
  --ink-dark:#333333;
  --paper:#ffffff;
  --soft:#f7f7f7;
}
*{margin:0;padding:0;box-sizing:border-box}
html,body{width:1200px;height:1075px;overflow:hidden;background:var(--paper)}
body{position:relative;font-family:"Open Sans",Arial,sans-serif;color:var(--ink)}
.abs{position:absolute}

/* header */
.brand{left:216px;top:112px;font-size:38px;font-weight:300;color:var(--green);letter-spacing:1px}
.social{display:flex;gap:6px}
.social span{width:19px;height:19px;border-radius:50%;background:var(--disc);display:block}
.social-head{left:404px;top:177px}
.account{left:560px;top:26px;font-size:11px;font-weight:600;color:var(--ink-dark)}
.account i{font-style:normal;margin:0 8px;font-weight:400}
.phone{right:172px;top:18px;font-size:23px;font-weight:300;color:var(--ink)}
.phone b{color:var(--green);font-weight:600;margin-right:8px}
.nav{left:518px;top:68px;width:510px;height:48px;background:var(--green);display:flex;align-items:center;justify-content:center;box-shadow:0 6px 8px -4px rgba(0,0,0,.25)}
.nav a{color:#fff;text-decoration:none;font-size:19px;font-weight:600;padding:0 13px;border-left:1px solid rgba(255,255,255,.4);line-height:12px}
.nav a:first-child{border-left:0}
.tagline{left:556px;top:126px;font-size:40px;font-weight:300;color:var(--green);white-space:nowrap}
.intro{left:561px;top:172px;font-size:22px;line-height:29px;color:var(--ink-dark);font-weight:300;width:460px}
.search{left:819px;top:265px;width:197px;height:21px;border:2px solid #bbb;border-radius:11px;background:#f1f1f1;font-size:11px;color:#666;padding:2px 0 0 8px}
.search svg{position:absolute;right:7px;top:3px}

/* feature band */
.band{left:0;top:281px;width:1200px;height:282px;background:var(--band)}
.video{left:195px;top:300px;width:387px;height:259px;background:#2b2b2b;border:6px solid #111;display:flex;align-items:center;justify-content:center}
.lead{left:622px;top:320px;font-size:26px;line-height:36px;color:#fff;width:380px}
.sub{left:624px;top:437px;font-size:20px;line-height:28px;color:#eee;font-weight:300;width:380px}
.sub strong{font-weight:400;color:#fff}
.consult{left:778px;top:535px;width:190px;height:50px;background:var(--green);color:#fff;font-size:20px;font-weight:600;display:flex;align-items:center;justify-content:center;z-index:2}

/* services */
.service{top:605px;width:260px;text-align:center}
.service .disc{width:124px;height:124px;border-radius:50%;background:var(--disc);margin:0 auto;display:flex;align-items:center;justify-content:center}
.service h2{font-size:24px;line-height:32px;font-weight:400;color:var(--green);margin-top:8px}
.service p{font-size:12.5px;line-height:20px;color:var(--ink);margin-top:12px;height:90px;padding:0 12px}
.service .btn{display:inline-block;width:146px;height:32px;line-height:32px;background:var(--green);color:#fff;font-size:14px;font-weight:600;margin-top:14px}
.divider{top:663px;height:254px;border-left:1px dotted #bbb}
.divider::before{content:"";position:absolute;left:-3px;top:0;width:5px;height:26px;background:var(--green)}

/* footer */
.foot-nav{left:196px;top:996px;font-size:14px;font-weight:600;color:#444}
.foot-nav span{padding:0 8px;border-left:1px solid #777;line-height:10px}
.foot-nav span:first-child{padding-left:0;border-left:0}
.copy{left:196px;top:1024px;font-size:13px;color:#555}
.social-foot{left:737px;top:1013px}
.foot-brand{left:845px;top:931px;width:332px;height:144px;background:var(--soft);padding:78px 0 0 22px}
.foot-brand span{font-size:22px;font-weight:300;color:var(--green);letter-spacing:1px}
</style>
</head>
<body>

<header>
  <div class="abs brand">HARBOURLIGHT</div>
  <div class="abs social social-head" aria-label="Social links"><span></span><span></span><span></span><span></span></div>
  <div class="abs account">Login<i>|</i>Register</div>
  <div class="abs phone"><b>M</b>0400 123 987</div>
  <nav class="abs nav"><a>HOME</a><a>ABOUT</a><a>SERVICES</a><a>CONTACT</a><a>FAQS</a></nav>
  <h1 class="abs tagline">Your wellness starts today</h1>
  <p class="abs intro">specialises in the treatment of Anxiety and Depression with a holistic approach</p>
</header>

<section class="abs band"></section>

<svg class="abs" style="left:0;top:240px" width="1200" height="50" viewBox="0 0 1200 50" aria-hidden="true">
  <path d="M171,20 Q480,12 790,17 Q480,21 171,41 Z" fill="var(--green)"/>
  <path d="M171,41 Q480,21 790,17 Q480,26 171,48 Z" fill="#fff"/>
</svg>

<div class="abs search">Search
  <svg width="13" height="13" viewBox="0 0 13 13"><circle cx="5" cy="5" r="4" fill="none" stroke="#444" stroke-width="1.6"/><line x1="8" y1="8" x2="12" y2="12" stroke="#444" stroke-width="2"/></svg>
</div>

<div class="abs video" role="img" aria-label="Introductory video about the practice">
  <svg width="60" height="60" viewBox="0 0 60 60"><circle cx="30" cy="30" r="29" fill="rgba(0,0,0,.6)"/><path d="M23,17 L44,30 L23,43 Z" fill="#fff"/></svg>
</div>
<p class="abs lead">Harbourlight Consulting is a highly professional, ethically bound business</p>
<p class="abs sub"><strong>MARA ELLIS commitment to provide quality healthcare</strong> for your whole family drives everything we do.</p>

<svg class="abs" style="left:0;top:563px" width="1200" height="30" viewBox="0 0 1200 30" aria-hidden="true">
  <path d="M420,0 C600,4 700,26 850,24 C950,22 990,10 1029,0 Z" fill="var(--green)"/>
</svg>
<div class="abs consult">CONSULT US</div>

<main>
  <div class="abs service" style="left:186px">
    <div class="disc"><svg width="80" height="80" viewBox="0 0 80 80" fill="none" stroke="var(--green)" stroke-width="4"><circle cx="40" cy="30" r="18"/><circle cx="30" cy="48" r="18"/><circle cx="50" cy="48" r="18"/></svg></div>
    <h2>Who We Are</h2>
    <p>Lorem ipsum dolor sit amet, consectetuer adipiscing elit, sed diam nonummy nibh euismod tincidunt ut laoreet dolore magna aliquam erat volutpat.</p>
    <span class="btn">GET TO KNOW US</span>
  </div>
  <div class="abs divider" style="left:451px"></div>
  <div class="abs service" style="left:461px">
    <div class="disc"><svg width="80" height="80" viewBox="0 0 80 80" stroke="var(--green)" stroke-width="4" fill="none"><line x1="40" y1="12" x2="40" y2="68"/><line x1="16" y1="26" x2="64" y2="54"/><line x1="16" y1="54" x2="64" y2="26"/><circle cx="40" cy="40" r="5" fill="var(--green)"/><circle cx="40" cy="10" r="4"/><circle cx="40" cy="70" r="4"/><circle cx="14" cy="25" r="4"/><circle cx="66" cy="55" r="4"/><circle cx="14" cy="55" r="4"/><circle cx="66" cy="25" r="4"/></svg></div>
    <h2>We’re Growing!</h2>
    <p>Ut wisi enim ad minim veniam, quis nostrud exerci tation ullamcorper suscipit lobortis nisl ut aliquip ex ea commodo consequat.</p>
    <span class="btn">HOW WE HELPS</span>
  </div>
  <div class="abs divider" style="left:724px"></div>
  <div class="abs service" style="left:730px">
    <div class="disc"><svg width="80" height="80" viewBox="0 0 80 80" fill="none" stroke="var(--green)" stroke-width="5"><circle cx="40" cy="40" r="30"/><circle cx="40" cy="40" r="17"/><circle cx="40" cy="40" r="6" fill="var(--green)"/></svg></div>
    <h2>Let’s Talk about You</h2>
    <p>Duis autem vel eum iriure dolor in hendrerit in vulputate velit esse molestie consequat, vel illum dolore eu feugiat nulla facilisis at vero eros et accumsan et iusto odio.</p>
    <span class="btn">CONSULT US</span>
  </div>
</main>

<footer>
  <div class="abs foot-nav"><span>HOME</span><span>ABOUT</span><span>SERVICES</span><span>CONTACT</span><span>FAQS</span></div>
  <div class="abs copy">Copyright © 2013 Harbourlight</div>
  <div class="abs social social-foot" aria-label="Social links"><span></span><span></span><span></span><span></span></div>
  <div class="abs foot-brand"><span>HARBOURLIGHT</span></div>
</footer>

</body>
</html>
```